Hartwell Taproom Co Menu Design

I have an exisiting restaurant called Hartwell Taproom Co. We have an official logo and an existing menu. We need something more professional and vibrant. We are a great little brewpub and need our menu to reflect the same.
Updates

I have added our existing menu that has our logo on first page. Please use and insert menu items and pricing. Thank you for all your help! I really need a great look... also our web site is hartwelltaproomco.comĀ  that may help as well

I have been trying to uplaod pictures for the menu design today but for some reason I can not get them to upload on this site. Will keep trying and hope to have some posted soon.

I have submitted pictures to pixel harbor web administration and they will be posting to my project shortly.

All pictures have been posted for menu design. Thanks!

Industry/Entity Type

Restaurant

Requirements
Must have
• Great layout with pictures!!! Need it to be eye catching with current menu items and pricing. Needs to be a funtional format so I can easily changed to add or delete items as needed. I am looking for a one page menu that is 8 1/2 x 14 with front and back side print that will be placed in a clear menu cover.

```html
<!DOCTYPE html>
<html lang="en">
<head>
<meta charset="utf-8">
<title>Hartwell Taproom Co Menu</title>
<link rel="stylesheet" href="https://fonts.googleapis.com/css2?family=Cinzel:wght@400;700&family=Open+Sans:wght@400;700&display=swap">
<style>
  :root {
    --canvas: #ffffff;
    --brick: #8e1a1c;
    --brick-dark: #5a0d0f;
    --panel: #000000;
    --heading-red: #d0262a;
    --item-orange: #f6a12c;
    --body-white: #ffffff;
  }
  * { box-sizing: border-box; margin: 0; padding: 0; }
  html, body { width: 1200px; height: 1000px; overflow: hidden; background: var(--canvas); }
  body { position: relative; font-family: "Open Sans", Verdana, sans-serif; color: var(--body-white); }

  .menu { position: absolute; left: 293px; top: 2px; width: 599px; height: 975px; overflow: hidden; }
  .brick-wall {
    position: absolute; inset: 0;
    background: radial-gradient(ellipse at center, var(--brick) 0%, var(--brick-dark) 100%);
  }
  .panel { position: absolute; left: 37px; top: 38px; width: 525px; height: 880px; background: var(--panel); }

  .column { position: absolute; top: 0; height: 860px; }
  .column-left { left: 70px; width: 236px; }
  .column-right { left: 298px; width: 230px; }
  .column > * { position: absolute; left: -10px; right: -10px; text-align: center; white-space: nowrap; }

  .section-title {
    font-family: "Cinzel", "Times New Roman", serif; color: var(--heading-red); font-weight: 400;
    font-size: 14px; letter-spacing: 0.8px; line-height: 13px; text-transform: uppercase;
  }
  .section-title.lunch { line-height: 13.5px; }
  .section-note { color: var(--heading-red); font-size: 11px; line-height: 12px; }
  .item-name { color: var(--item-orange); font-weight: 700; font-size: 11.5px; line-height: 13px; }
  .item-desc { font-size: 10.5px; line-height: 11.6px; }
  .item-price { font-weight: 700; font-size: 12px; line-height: 14px; }

  .brand-mark { position: absolute; left: 322px; top: 630px; width: 200px; display: flex; flex-direction: column; align-items: center; gap: 14px; }
  .brand-dot { width: 90px; height: 90px; border-radius: 50%; background: var(--heading-red); }
  .brand-name { font-weight: 700; font-size: 20px; line-height: 24px; color: var(--item-orange); text-align: center; white-space: nowrap; }

  .food-strip {
    position: absolute; left: 4px; top: 860px; width: 595px; height: 115px;
    background: linear-gradient(90deg, #e8c25a 0%, #7a4a2a 22%, #c9782c 40%, #a8331e 55%, #5e8a3a 75%, #e9e4d2 100%);
  }
</style>
</head>
<body>
  <main class="menu">
    <div class="brick-wall" role="img" aria-label="Red brick wall background texture"></div>
    <div class="panel"></div>

    <section class="column column-left">
      <h2 class="section-title" style="top:55.5px">Personal Pizzas<br>(7 inch)</h2>
      <p class="section-note" style="top:83px">*7 inch pizza and side salad<br>combo for $8.25</p>

      <p class="item-name" style="top:113.5px">Portabella Roasted Red<br>Pepper Pizza</p>
      <p class="item-desc" style="top:140.2px">Basil pesto, mozzarella, red peppers, porta-<br>bella mushroom, baby greens and<br>parmesan cheese</p>
      <p class="item-price" style="top:176px">$7.25</p>

      <p class="item-name" style="top:192.5px">Margarita Pizza</p>
      <p class="item-desc" style="top:206.2px">Garlic infused olive oil, tomato sauce, mozza-<br>rella cheese, sliced tomatoes and pesto</p>
      <p class="item-price" style="top:231px">$6.95</p>

      <p class="item-name" style="top:249.5px">BBQ Buffalo Chicken Pizza</p>
      <p class="item-desc" style="top:263.2px">BBQ sauce, mozzarella, diced celery, red<br>onions and grilled chicken breast marinated in<br>buttery buffalo sauce drizzled with ranch<br>dressing</p>
      <p class="item-price" style="top:310px">$7.25</p>

      <p class="item-name" style="top:329.5px">Bleu Fire Chicken Pizza</p>
      <p class="item-desc" style="top:344.2px">Fire glaze, mozzarella, bleu cheese, cheddar<br>jack, portabella mushroom, mesquite chicken,<br>scallions and cilantro</p>
      <p class="item-price" style="top:381px">$7.25</p>

      <h2 class="section-title lunch" style="top:401.3px">Lunch Specials<br>Monday - Friday<br>11:00am - 3:00pm</h2>
      <p class="section-note" style="top:443px">(No Substitutions)</p>

      <p class="item-name" style="top:462.5px">Chicken Ceasar Salad</p>
      <p class="item-desc" style="top:477.2px">(Lunch portion): Romaine lettuce and mesquite<br>grilled chicken, focaccia croutons, parmesan<br>cheese and Caesar dressing</p>
      <p class="item-price" style="top:515px">$5.95</p>

      <p class="item-name" style="top:531.5px; line-height:12.5px">Tinga De Pollo Quesadilla &amp; House<br>Side Salad</p>
      <p class="item-desc" style="top:556.2px">Grilled chicken is made in a cream sauce with<br>caramelized onions, roasted peppers, smoked<br>jalapeno, cilantro and Colby jack cheese on a<br>flour tortilla and chipotle dipping sauce</p>
      <p class="item-price" style="top:603px">$5.95</p>

      <p class="item-name" style="top:626.5px">Half Grilled Sandwich Combo</p>
      <p class="item-desc" style="top:639.2px">Choose from Pastrami and Swiss on rye with<br>mustard and sauerkraut &nbsp;- &nbsp;OR - &nbsp;Chicken<br>Caprese made with basil pesto, tomatoes and<br>provolone on a French baguette. Comes with<br>fries and house side salad</p>
      <p class="item-price" style="top:696px">$6.95</p>

      <p class="item-name" style="top:716.5px">Bottomless Soup And Salad</p>
      <p class="item-desc" style="top:730.2px">Soup of the day and our house side salad<br>made with romaine, diced tomatoes, and<br>crumbled bleu cheese<br>(Lobster Bisque $1.00 extra)</p>
      <p class="item-price" style="top:777px">$7.95</p>

      <p class="item-name" style="top:795.5px">Grilled Salmon Tacos</p>
      <p class="item-desc" style="top:809.2px">2 grilled Alaskan wild salmon tacos topped<br>with pico de gallo and chipotle ranch and<br>house side salad</p>
      <p class="item-price" style="top:843px">$5.95</p>
    </section>

    <section class="column column-right">
      <p class="item-name" style="top:56.5px">Margarita Pizza &amp; House Side Salad</p>
      <p class="item-desc" style="top:70.2px; line-height:13px">Made with basil pesto, mozzarella, tomatoes,<br>marinara and house side salad</p>
      <p class="item-price" style="top:96px">$5.95</p>

      <h2 class="section-title" style="top:113.5px">Kids 12 and Under<br><span style="font-size:12px">Includes Drink - $6.75</span></h2>
      <p class="item-name" style="top:151.5px">Cheese Pizza</p>
      <p class="item-name" style="top:175.5px">Smoke House Mac &amp; Cheese</p>
      <p class="item-name" style="top:199.5px">JR Cheese Burger (with lettuce,<br>tomato and mayo) &amp; Fries</p>
      <p class="item-name" style="top:239.5px">Grilled Cheese On Sourdough<br>&amp; Fries</p>
      <p class="item-name" style="top:276.5px">Grilled Chicken Sandwich &amp; Fries (on<br>Sourdough with cheddar cheese,<br>lettuce, tomato and mayo)</p>

      <h2 class="section-title" style="top:324.5px">Beverages</h2>
      <p class="item-desc" style="top:342.2px">Koala Cola, Diet Koala Cola, Spritz Lime,<br>Mr. Piper, Barrows Rootbeer, Lemonade<br>and Strawberry Lemonade</p>
      <p class="item-price" style="top:377px">$2.25</p>
      <p class="item-desc" style="top:397.2px"><b>Iced Tea:</b> Regular, Peach, Raspberry</p>
      <p class="item-price" style="top:410px">$2.25</p>
      <p class="item-desc" style="top:429.2px"><b>Juice:</b> Apple, Crangrape</p>
      <p class="item-price" style="top:442px">$1.75</p>
      <p class="item-desc" style="top:463.2px">Milk / Chocolate Milk</p>
      <p class="item-price" style="top:477px">$1.75</p>

      <h2 class="section-title" style="top:497.5px">Dessert</h2>
      <p class="item-name" style="top:516.5px">CHOCOLATE LAVA CAKE</p>
      <p class="item-desc" style="top:532.2px">Served with whip cream, powder sugar and<br>chocolate sauce drizzle</p>
      <p class="item-price" style="top:556px">$4.95</p>
    </section>

    <div class="brand-mark">
      <span class="brand-dot"></span>
      <p class="brand-name">Hartwell Taproom Co</p>
    </div>

    <div class="food-strip" role="img" aria-label="Photo strip of dishes: mac and cheese, sandwich, beers, chicken wings, salads"></div>
  </main>
</body>
</html>
```